Bobcat / excavator / tipper contractor
info for back of card {
2.3 ton bobcat 1.6m wide
3.6 ton excavator 1.6 wide
4.5M tipper 2.4 wide }
In the industry since 1999
Experienced in all aspects of bobcat excavator general hire work
Brisbane to goldcoast area
competitive rates

As for the image uploaded, I kind of like the H made out of the bulidings and the brown and yellow are the colors of my footy team. but open to anything that is unique the portrays excavation that can become a symbol for my business.so the H is good or something with DMR.

Im wanting to create business cards and either large magnets or a wrap for the front of the truck.
dresfordmachinerental @ examplemail . test

Contractor

Luke Dresford
Dresford Machine Rental Pty Ltd
ABN 51830296714
mobile 0491326048
dresfordmachinerental@examplemail.test

```html
<!DOCTYPE html>
<html lang="en">
<head>
<meta charset="utf-8">
<title>Dresford Machine Rental – Business Card</title>
<link rel="stylesheet" href="https://fonts.googleapis.com/css2?family=PT+Sans:wght@400;700&family=Roboto+Condensed:wght@400;700&family=Open+Sans:wght@400&display=swap">
<style>
  :root {
    --card-sand: #dec8a6;
    --brand-brown: #4b2a17;
    --brand-orange: #f08a24;
  }
  html, body {
    margin: 0;
    padding: 0;
    overflow: hidden;
    background: var(--card-sand);
  }
  .card {
    position: relative;
    width: 1200px;
    height: 698px;
    background: var(--card-sand);
    overflow: hidden;
  }
  .brand {
    position: absolute;
    left: 60px;
    top: 200px;
    width: 432px;
    text-align: center;
  }
  .brand-mark {
    display: inline-flex;
    align-items: center;
    gap: 16px;
    height: 210px;
  }
  .brand-initials {
    font-family: "PT Sans", sans-serif;
    font-weight: 700;
    font-size: 120px;
    letter-spacing: 4px;
    color: var(--brand-brown);
    line-height: 1;
  }
  .brand-square {
    width: 28px;
    height: 28px;
    background: var(--brand-orange);
    align-self: flex-end;
    margin-bottom: 56px;
  }
  .brand-name {
    margin-top: 14px;
    font-family: "Open Sans", sans-serif;
    font-weight: 400;
    font-size: 20px;
    color: var(--brand-orange);
    white-space: nowrap;
    line-height: 1;
  }
  .person {
    position: absolute;
    left: 642px;
    top: 206px;
  }
  .person-name {
    margin: 0;
    font-family: "PT Sans", sans-serif;
    font-weight: 700;
    font-size: 56px;
    line-height: 1;
    color: var(--brand-brown);
    white-space: nowrap;
  }
  .person-role {
    margin: 6px 0 0 2px;
    font-family: "Open Sans", sans-serif;
    font-size: 23px;
    line-height: 1;
    color: var(--brand-orange);
  }
  .contact {
    position: absolute;
    left: 644px;
    top: 334px;
    margin: 0;
    display: grid;
    grid-template-columns: 125px auto;
    row-gap: 10px;
    font-family: "Roboto Condensed", sans-serif;
    font-size: 28px;
    line-height: 36px;
  }
  .contact dt {
    font-weight: 700;
    color: var(--brand-brown);
  }
  .contact dd {
    margin: 0;
    color: var(--brand-orange);
    white-space: nowrap;
  }
  .contact .contact-email {
    font-size: 23px;
  }
  .band-orange {
    position: absolute;
    left: 0;
    top: 656px;
    width: 1200px;
    height: 14px;
    background: var(--brand-orange);
  }
  .band-brown {
    position: absolute;
    left: 0;
    top: 670px;
    width: 1200px;
    height: 28px;
    background: var(--brand-brown);
  }
</style>
</head>
<body>
  <main class="card">
    <section class="brand">
      <div class="brand-mark">
        <span class="brand-initials">DMR</span>
        <span class="brand-square"></span>
      </div>
      <div class="brand-name">DRESFORD MACHINE RENTAL PTY LTD</div>
    </section>

    <section class="person">
      <h1 class="person-name">LUKE DRESFORD</h1>
      <p class="person-role">DIRECTOR</p>
    </section>

    <dl class="contact">
      <dt>Mobile</dt>
      <dd>0491 326 048</dd>
      <dt>Email</dt>
      <dd class="contact-email">dresfordmachinerental@examplemail.test</dd>
      <dt>ABN</dt>
      <dd>51830296714</dd>
    </dl>

    <div class="band-orange"></div>
    <div class="band-brown"></div>
  </main>
</body>
</html>
```